Landscape install that wants to be known for specializing in backyard oasis

I install high end backyard retreats, I also instal water features, kitchens, patio and plants, I am not a landscaper that cuts grass for a source of income but I want to be know as someone who could be the first company you think of when you want any form of hard scape installed. Up to this point my projects have required a creative custom install that is different to cookie cutter install companies, I chose the name to reflect a company that is professional but also let customer know that I work and specialize in stone install

Target Market(s)

To everyone but more important is target customers and professionals that my company is the one they should choose

Industry/Entity Type

Landscape

Contact Information for Business Card

Dennis Markham
2847 Tindle Ct
Elmsworth, OH 43917
Email: www.bluefernyardcraft@quillpost.com

Requirements
Must have
• If you could help with a signature logo or something current and relevant
Nice to have
• Creative layout of the card with an great backdrop that reflects the company as cutting edge and current

```html
<!DOCTYPE html>
<html lang="en">
<head>
<meta charset="utf-8">
<title>Bluefern Yardcraft – Business Card</title>
<link rel="stylesheet" href="https://fonts.googleapis.com/css2?family=Questrial&display=swap">
<style>
  :root {
    --page-bg: #e9e6e1;
    --card-white: #ffffff;
    --card-fade: #ececec;
    --panel-grey: #e3e3e3;
    --stone-dark: #2b2f33;
    --stone-mid: #4a5157;
    --stone-light: #6c747a;
    --ink-dark: #2e2e2e;
    --ink-name: #8c8c8c;
    --ink-detail: #4d4d4d;
    --wordmark-light: #e6e8ea;
  }
  * { box-sizing: border-box; margin: 0; padding: 0; }
  html, body {
    width: 1200px;
    height: 784px;
    overflow: hidden;
    background: var(--page-bg);
    font-family: "Questrial", "Century Gothic", sans-serif;
  }
  .canvas {
    position: relative;
    width: 1200px;
    height: 784px;
  }
  .card {
    position: absolute;
    top: 238px;
    width: 540px;
    height: 308px;
    overflow: hidden;
    box-shadow: 0 6px 18px rgba(0, 0, 0, 0.18);
  }

  /* Back of card */
  .card--back { left: 40px; }
  .stone-surface {
    position: absolute;
    inset: 0;
    background: radial-gradient(ellipse at 50% 45%, var(--stone-light) 0%, var(--stone-mid) 45%, var(--stone-dark) 100%);
  }
  .back-wordmark {
    position: absolute;
    inset: 0;
    display: flex;
    align-items: center;
    justify-content: center;
    gap: 14px;
  }
  .back-wordmark__square {
    width: 34px;
    height: 34px;
    background: var(--wordmark-light);
  }
  .back-wordmark__name {
    font-size: 34px;
    color: var(--wordmark-light);
    letter-spacing: 0.5px;
  }

  /* Front of card */
  .card--front {
    left: 620px;
    background: linear-gradient(160deg, var(--card-white) 0%, var(--card-white) 45%, var(--card-fade) 100%);
  }
  .front-panel {
    position: absolute;
    top: 0;
    right: 0;
    width: 190px;
    height: 268px;
    background: linear-gradient(180deg, var(--panel-grey) 0%, rgba(227, 227, 227, 0.35) 100%);
  }
  .brand {
    position: absolute;
    top: 40px;
    left: 34px;
    display: flex;
    align-items: center;
    gap: 14px;
  }
  .brand__square {
    width: 44px;
    height: 44px;
    background: var(--stone-dark);
  }
  .brand__name {
    font-size: 28px;
    color: var(--ink-dark);
  }
  .contact {
    position: absolute;
    left: 34px;
    top: 160px;
  }
  .contact__person {
    font-size: 22px;
    color: var(--ink-name);
    margin-bottom: 16px;
  }
  .contact__line {
    display: flex;
    align-items: center;
    gap: 8px;
    font-size: 18px;
    color: var(--ink-detail);
    margin-bottom: 8px;
    white-space: nowrap;
  }
  .contact__line svg { width: 16px; height: 16px; fill: var(--ink-detail); flex: none; }
  .stone-band {
    position: absolute;
    left: 0;
    right: 0;
    bottom: 0;
    height: 40px;
    background: linear-gradient(90deg, var(--stone-dark) 0%, var(--stone-mid) 50%, var(--stone-dark) 100%);
  }
</style>
</head>
<body>
<main class="canvas">

  <section class="card card--back" aria-label="Back of business card">
    <div class="stone-surface" role="img" aria-label="Dark slate stone wall texture"></div>
    <div class="back-wordmark">
      <span class="back-wordmark__square"></span>
      <span class="back-wordmark__name">Bluefern Yardcraft</span>
    </div>
  </section>

  <section class="card card--front" aria-label="Front of business card">
    <div class="front-panel"></div>

    <div class="brand">
      <span class="brand__square"></span>
      <span class="brand__name">Bluefern Yardcraft</span>
    </div>

    <div class="contact">
      <p class="contact__person">Dennis Markham</p>
      <p class="contact__line">
        <svg viewBox="0 0 24 24" aria-hidden="true"><path d="M6.6 10.8a15.1 15.1 0 0 0 6.6 6.6l2.2-2.2a1 1 0 0 1 1-.25 11.4 11.4 0 0 0 3.6.57 1 1 0 0 1 1 1V20a1 1 0 0 1-1 1A17 17 0 0 1 3 4a1 1 0 0 1 1-1h3.5a1 1 0 0 1 1 1c0 1.25.2 2.45.57 3.57a1 1 0 0 1-.25 1z"/></svg>
        1472 903 518
      </p>
      <p class="contact__line">
        <svg viewBox="0 0 24 24" aria-hidden="true"><path d="M12 3 2 12h3v8h5v-6h4v6h5v-8h3z"/></svg>
        2847 Tindle Ct Elmsworth, OH 43917
      </p>
    </div>

    <div class="stone-band" role="img" aria-label="Strip of dark slate stone wall texture"></div>
  </section>

</main>
</body>
</html>
```